Veterinary Clinic Letterhead - Ridgeview Veterinary Surgery

We need a letterhead design for an established Veterinary Clinic in Kallinda called Ridgeview Veterinary Surgery. We are a moderate sized mixed animal veterinary clinic offering a wide variety of veterinary services. The design should use the same colour pattern as those in the logos supplied. The design should also include our address (48 Tulloch Road, Kallinda, Northvale, 4875), phone number (07 4158 6734), email (admin@ridgeviewvets.com.au), website (www.ridgeviewvets.com.au) and our opening hours (8am to 5pm Monday to Friday and 8am to 12pm Saturday).
Target Market(s)
Pet owners
Industry/Entity Type
Veterinary
Requirements
Must have
- The logo or modification of it, business address, opening hours, website, phone number and email address

```html
<!DOCTYPE html>
<html lang="en">
<head>
<meta charset="utf-8">
<title>Ridgeview Veterinary Surgery – Letterhead</title>
<link href="https://fonts.googleapis.com/css2?family=Roboto:wght@300;400;500;700&family=Pinyon+Script&display=swap" rel="stylesheet">
<style>
  :root {
    --backdrop: #e4e4e4;
    --paper: #f2f2f2;
    --navy: #0c2447;
    --blue: #0a4a9a;
    --sky: #0b73b3;
    --pale-blue: #76a6d0;
    --body-text: #2a2a2a;
    --footer-text: #6b6b6b;
    --divider: #b5b5b5;
    --faint-mark: rgba(0, 0, 0, 0.045);
  }
  * { box-sizing: border-box; margin: 0; padding: 0; }
  html, body {
    width: 1200px; height: 1200px; overflow: hidden;
    background: var(--backdrop);
  }
  .letterhead {
    position: absolute; left: 203px; top: 40px;
    width: 794px; height: 1120px;
    background: var(--paper);
    box-shadow: 0 2px 12px rgba(0,0,0,0.12);
    font-family: "Roboto", sans-serif;
    font-weight: 300;
    color: var(--body-text);
    overflow: hidden;
  }
  .brand {
    position: absolute; left: 0; right: 0; top: 28px;
    display: flex; flex-direction: column; align-items: center;
  }
  .brand-dot {
    width: 84px; height: 84px; border-radius: 50%;
    background: var(--navy);
  }
  .brand-name {
    margin-top: 9px;
    font-weight: 700; font-size: 14.5px; line-height: 1.15;
    letter-spacing: 0.4px; text-transform: uppercase;
    color: var(--navy); text-align: center;
  }
  .faint-mark {
    position: absolute; left: 222px; top: 383px;
    width: 306px; height: 306px; border-radius: 50%;
    background: var(--faint-mark);
  }
  .letter {
    position: absolute; left: 85px; width: 624px;
    font-size: 13.2px; line-height: 18.7px;
  }
  p.letter { text-align: justify; }
  .date { top: 264px; }
  .recipient { top: 302px; }
  .salutation { top: 395px; }
  .para-1 { top: 432px; }
  .para-2 { top: 581px; }
  .para-3 { top: 693px; }
  .closing { top: 842px; }
  .signature {
    position: absolute; left: 85px; top: 862px;
    font-family: "Pinyon Script", cursive;
    font-size: 25px; color: #1a1a1a;
  }
  .footer {
    position: absolute; left: 85px; right: 85px; top: 1030px;
    font-size: 13px; line-height: 16.2px; color: var(--footer-text);
    font-weight: 400;
  }
  .contact-list { position: absolute; left: 0; top: 0; list-style: none; }
  .contact-list li { display: flex; align-items: center; gap: 7px; }
  .contact-list svg { width: 11px; height: 11px; fill: var(--footer-text); }
  .footer-divider {
    position: absolute; left: 202px; top: 2px;
    width: 1px; height: 44px; background: var(--divider);
  }
  .address { position: absolute; left: 220px; top: 0; font-style: normal; }
  .hours { position: absolute; right: 0; top: 0; text-align: right; }
  .hours strong { font-weight: 700; }
  .colour-bands {
    position: absolute; left: 0; right: 0; bottom: 0; height: 13px;
    display: flex;
  }
  .colour-bands span { flex: 1; }
  .band-navy { background: var(--navy); }
  .band-blue { background: var(--blue); }
  .band-sky { background: var(--sky); }
  .band-pale { background: var(--pale-blue); }
</style>
</head>
<body>
<main class="letterhead">
  <header class="brand">
    <div class="brand-dot"></div>
    <div class="brand-name">Ridgeview Veterinary<br>Surgery</div>
  </header>

  <div class="faint-mark"></div>

  <div class="letter date">01 January 2050</div>
  <div class="letter recipient">Company (Pvt) Ltd.<br>PO Box 3355 Harlow St<br>Sample City Country 3355</div>
  <div class="letter salutation">Dear Daniel Harcourt,</div>
  <p class="letter para-1">Lorem ipsum dolor sit amet, consectetuer adipiscing elit, sed diam nonummy nibh euismod tincidunt ut laoreet dolore magna aliquam erat volutpat. Ut wisi enim ad minim veniam, quis nostrud exerci tation ullamcorper suscipit lobortis nisl ut aliquip ex ea commodo consequat. Duis dolore te feugait nulla facilisi. Nam liber tempor cum soluta nobis eleifend option congue nihil imperdiet doming id quod mazim placerat facer possim assum. Lorem ipsum dolor sit amet, consectetuer adipiscing elit, sed diam nonummy nibh euismod tincidunt ut laoreet dolore magna aliquam erat volutpat. Ut wisi enim ad minim veniam, quis nostrud exerci tation ullamcorper suscipit lobortis nisl ut aliquip ex ea commodo consequat.</p>
  <p class="letter para-2">Consectetuer adipiscing elit, sed diam nonummy nibh euismod tincidunt ut laoreet dolore magna aliquam erat volutpat. Ut wisi enim ad minim veniam, quis nostrud exerci tation ullamcorper suscipit lobortis nisl ut aliquip ex ea commodo consequat. Consectetuer adipiscing elit, sed diam nonummy nibh euismod tincidunt ut laoreet dolore magna aliquam erat volutpat. Ut wisi enim ad minim veniam, quis nostrud exerci tation ullamcorper suscipit lobortis nisl ut aliquip ex ea commodo consequat.</p>
  <p class="letter para-3">Consectetuer adipiscing elit, sed diam nonummy nibh euismod tincidunt ut laoreet dolore magna aliquam erat volutpat. Ut wisi enim ad minim veniam, quis nostrud exerci tation ullamcorper suscipit lobortis nisl ut aliquip ex ea commodo consequat. Consectetuer adipiscing elit, sed diam nonummy nibh euismod tincidunt ut laoreet dolore magna aliquam erat volutpat. Ut wisi enim ad minim veniam, quis nostrud exerci tation ullamcorper suscipit lobortis nisl ut aliquip ex ea commodo consequat.</p>
  <div class="letter closing">Sincerely Yours</div>
  <div class="signature">Thomas Whitfield</div>

  <footer class="footer">
    <ul class="contact-list">
      <li><svg viewBox="0 0 24 24"><path d="M6.6 10.8a15.1 15.1 0 0 0 6.6 6.6l2.2-2.2a1 1 0 0 1 1-.25 11.4 11.4 0 0 0 3.6.57 1 1 0 0 1 1 1V20a1 1 0 0 1-1 1A17 17 0 0 1 3 4a1 1 0 0 1 1-1h3.5a1 1 0 0 1 1 1c0 1.25.2 2.45.57 3.57a1 1 0 0 1-.25 1z"/></svg>07 4158 6734</li>
      <li><svg viewBox="0 0 24 24"><path d="M2 5h20v14H2zM3.5 6.5 12 13l8.5-6.5z" fill-rule="evenodd"/></svg>admin@ridgeviewvets.com.au</li>
      <li><svg viewBox="0 0 24 24"><path d="M12 2a10 10 0 1 0 0 20 10 10 0 0 0 0-20zm-1 2.1V8H7.6A8 8 0 0 1 11 4.1zm2 0A8 8 0 0 1 16.4 8H13zM4.3 10h6.7v4H4.3a8 8 0 0 1 0-4zm8.7 0h6.7a8 8 0 0 1 0 4H13zm-5.4 6H11v3.9A8 8 0 0 1 7.6 16zm5.4 0h3.4a8 8 0 0 1-3.4 3.9z"/></svg>www.ridgeviewvets.com.au</li>
    </ul>
    <div class="footer-divider"></div>
    <address class="address">48 Tulloch Road<br>Kallinda<br>Northvale, 4875</address>
    <div class="hours"><strong>Our Opening Hours:</strong><br>8am to 5pm (Monday to Friday)<br>8am to 12pm (Saturday)</div>
  </footer>

  <div class="colour-bands">
    <span class="band-navy"></span><span class="band-blue"></span><span class="band-sky"></span><span class="band-pale"></span>
  </div>
</main>
</body>
</html>
```